BRQL project
Cloudward Trainer Bench Systems
i dont see, button or anything ,,,...
about handover...anyone help me..??
i am first in here..how way the rule and upload my file to ch....
The project has been extended for 3 more days.
Ruth.
Hi,
I want only static
hello ! my name is Ida :) I want to participate this nice contest ~! Haven't one .ai format logo ? I not understand static or animated banner !? please more details - thanks
or not of*
flash of animated gif?
I would like to see it animated also
Do you need it animated?
I would like to see also a new with the wgt lifter text to be replaced by Vortek WGT PC.
Also add the bellow text
Increase WGT performance by 30% and more
It would be great if you could give specific text content / copy. Please mention your preferred colors and other specifications(if any). A more detailed design brief would help.

```html
<!DOCTYPE html>
<html lang="en">
<head>
<meta charset="utf-8">
<title>BRQL – Vortek WGT PC banner set</title>
<link rel="stylesheet" href="https://fonts.googleapis.com/css2?family=Roboto+Condensed:wght@400;700&display=swap">
<style>
  :root {
    --canvas: #8c8c8c;
    --blue-deep: #0b178a;
    --blue-mid: #1c33c4;
    --blue-bright: #3a5cf0;
    --sky-light: #b9c6f5;
    --white: #ffffff;
    --navy: #0d1a6e;
  }
  * { box-sizing: border-box; margin: 0; padding: 0; }
  html, body { width: 1200px; height: 845px; overflow: hidden; }
  body {
    background: var(--canvas);
    position: relative;
    font-family: "Roboto Condensed", "Arial Narrow", sans-serif;
    color: var(--white);
  }
  .banner {
    position: absolute;
    overflow: hidden;
    background: linear-gradient(160deg, var(--blue-bright) 0%, var(--blue-mid) 45%, var(--blue-deep) 100%);
    box-shadow: 0 0 10px rgba(0,0,0,.35);
  }
  .jet-visual {
    position: absolute;
    background: radial-gradient(ellipse at 55% 45%, var(--white) 0%, var(--sky-light) 22%, var(--blue-bright) 55%, transparent 80%);
  }
  .corner-swoosh { position: absolute; background: var(--white); border-radius: 50%; }
  .brand-mark {
    position: absolute;
    display: flex; align-items: center; gap: 6px;
    color: var(--navy); font-weight: 700; letter-spacing: 1px;
  }
  .brand-mark .dot { width: 14px; height: 14px; border-radius: 50%; background: var(--navy); }
  .headline, .subline, .offer { position: absolute; text-transform: none; line-height: 1; text-shadow: 0 1px 3px rgba(0,0,20,.5); }
  .headline { font-weight: 700; text-transform: uppercase; }
  .subline { font-weight: 700; text-transform: uppercase; }
  .offer { font-weight: 700; }
  .offer .pct { font-size: 1.9em; }

  /* skyscraper */
  .sky { left: 53px; top: 72px; width: 200px; height: 740px; }
  .sky .jet-visual { left: -60px; top: 0; width: 320px; height: 320px; }
  .sky .headline { left: 0; width: 100%; top: 316px; text-align: center; font-size: 50px; }
  .sky .subline { left: 0; width: 100%; top: 442px; text-align: center; font-size: 26px; line-height: 1.15; }
  .sky .offer { left: 0; width: 100%; top: 512px; text-align: center; font-size: 30px; }
  .sky .offer .pct { font-size: 64px; }
  .sky .offer-tail { display: block; font-size: 28px; margin-top: 2px; }
  .sky .corner-swoosh { left: -80px; top: 640px; width: 360px; height: 260px; }
  .sky .brand-mark { left: 60px; top: 680px; font-size: 22px; }

  /* leaderboard */
  .leader { left: 264px; top: 72px; width: 821px; height: 108px; }
  .leader .jet-visual { left: -40px; top: -80px; width: 300px; height: 260px; }
  .leader .headline { left: 204px; top: 16px; font-size: 40px; letter-spacing: .5px; }
  .leader .subline { left: 204px; top: 60px; font-size: 23px; }
  .leader .offer { left: 600px; top: 14px; font-size: 28px; }
  .leader .offer .pct { font-size: 44px; }
  .leader .offer-tail { display: block; font-size: 28px; margin-left: 10px; }
  .leader .corner-swoosh { left: 730px; top: -60px; width: 260px; height: 240px; }
  .leader .brand-mark { left: 752px; top: 40px; font-size: 20px; }

  /* square */
  .square { left: 264px; top: 204px; width: 372px; height: 305px; }
  .square .jet-visual { left: -40px; top: -40px; width: 320px; height: 220px; }
  .square .headline { left: 0; width: 100%; top: 150px; text-align: center; font-size: 44px; }
  .square .subline { left: 0; width: 100%; top: 200px; text-align: center; font-size: 25px; }
  .square .offer { left: 0; width: 100%; top: 226px; text-align: center; font-size: 27px; }
  .square .offer .pct { font-size: 46px; }
  .square .corner-swoosh { left: 250px; top: -120px; width: 240px; height: 220px; }
  .square .brand-mark { left: 284px; top: 36px; font-size: 20px; }
</style>
</head>
<body>
  <section class="banner sky">
    <div class="jet-visual" role="img" aria-label="Photo of a white business jet nose angled toward the viewer"></div>
    <h1 class="headline">Vortek<br>WGT PC</h1>
    <p class="subline">Increase WGT<br>Performance</p>
    <p class="offer">by <span class="pct">30%</span><span class="offer-tail">and more!</span></p>
    <div class="corner-swoosh"></div>
    <div class="brand-mark"><span class="dot"></span>BRQL</div>
  </section>

  <section class="banner leader">
    <div class="jet-visual" role="img" aria-label="Photo of a white business jet nose angled toward the viewer"></div>
    <h1 class="headline">Vortek WGT PC</h1>
    <p class="subline">Increase WGT Performance</p>
    <p class="offer">by <span class="pct">30%</span><span class="offer-tail">and more!</span></p>
    <div class="corner-swoosh"></div>
    <div class="brand-mark"><span class="dot"></span>BRQL</div>
  </section>

  <section class="banner square">
    <div class="jet-visual" role="img" aria-label="Photo of a white business jet nose angled toward the viewer"></div>
    <div class="corner-swoosh"></div>
    <div class="brand-mark"><span class="dot"></span>BRQL</div>
    <h1 class="headline">Vortek WGT PC</h1>
    <p class="subline">Increase WGT Performance</p>
    <p class="offer">by <span class="pct">30%</span> and more!</p>
  </section>
</body>
</html>
```